Makeup brushes and lashes brochure for vibrant new brand!

(UPDATE we have added a sample brochure for your guidance. Similar layout required,brush description is not necessary in lengthy form,brush number and title is acceptable))We are looking for an enthusiastic designer to work with us on our new 3fold brochure of our products. The brochure will be included in customers orders to entice them to make more purchases. All products must be displayed in along witglh the product name/ numbers.

We have three product ranges,makeup brushes,false lashes and cosmetic sponge. The brochure should tie in with our other packaging themes and be clear and modern.

The following information is required:

Company description-
Established in 2015 by Professional Makeup Artist Maura Delaney, Dab&Glow is one of Irelands leading cosmetic brands. We provide the beauty industry with incredibly high quality makeup brushes and Luxury Lashes.
Expertly design by Maura and handmade using incredibly high quality natural and synthetic hair.

Brush Care-(To be placed after brush imagery and descriptions.)

Keep'em clean! To keep your brushes in their best shape possible,clean them once a week with warm soapy water. Avoid submerging the ferrule Metal part) in water as this could loosen the glue inside and cause the hair to shed. Shedding is normal for the first few washes.
Rinse the brush well with clean water and air dry flat.

Lash Care-( To be placed after lash imagery and descriptions.)

All our lashes are re-usable so take care of them and you will have fluttery long lashes for up to 30 wears!

We recommend cleaning your lashes after every 3 wears.

Firstly, remove any left over glue from the lash band and soak the lashes in warm soapy water for 5 minutes. Remove and rinse and residue from the lash. re-Shape and Replace the lash back into its case and let dry naturally. As good as new!

Brushes descriptions- (Please crop brush images to below logo on handle.)

BRUSH SETS

Quite Rosy Glow - Containing 8 professional brushes,this set is your go to for your everyday makeup application. DG01,DG02 , DG03,DG04,DG05,DG06,DG10,DG24

Top Lids Set- Contain 8 of our incredible eye brushes for expert application. DG02,DG06,DG12,DG14,DG16,DG18,DG20,DG24

Sharp Cheek set- The ideal mix containing 6 of our most popular face and eye brushes. DG07,DG09,DG14,DG16,DG18,DG24.

INDIVIDUAL BRUSHES

DG01- Large synthetic powder brush. Ideal for use with powder foundations,creams or liquids.

DG02- Ideal for detailed eye work, Using ultra soft hair ,it won't irritate the delicate eye area.

DG03- Domed Shape,synthetic hair, the DG03 is perfect for seamlessly buffing liquid,creams,gel based foundations into the skin for a flawless finish.

DG04- Ultra soft synthetic hair,DG04 is a must have multi task brush. From concealer to eyeshadow application this all rounder is essential in the makeup bag.

DG05- Silky soft blush brush applies the perfect amount of product for flawless skin.

DG06- Precisely blends shadows into the socket of the eye for controlled blending.

DG08- NEW!(BOLD Writing) Domed shadow blending brush,ideal for softening edges.

DG09- The unique tapered shape on our contour is perfect for chiseling out cheekbones or simply adding a pop of colour to the cheeks using the flat sides. (Synthetic)

DG10- Synthetic hair,DG10 is ultra thin with a precise angle ,ideal for creating winged eyeliner or definition to brows.

DG12- Our finest blending brush yet! This truly is a must have for anyone who loves to add precise detail to their makeup looks. Super soft and light, it blends with ease for a flawless finish.

DG14- This is the ultimate brush for under eye blending! Dense, silky and sturdy, it is simply an essential in any eye look.

DG16- Another must have for any makeup bag is our flat shading brush. No more fall out from eyeshadows as this controls the placement perfectly.( Synthetic)

DG18- If your looking to pack on colour to a specific area or to smudge out for a smokey effect this nifty little brush is one for the collection.(Synthetic)

DG20- An all rounder brush, our flat definer is a real multitasker. From defining the brows to cutting the crease there is no job too big or too small for the DG20. (Synthetic)

DG24- Ultra soft and dense. Hand crafted ,tapered hair blends shadows effortlessly.

LASHES
3 lash ranges-
VelTrim-
Luxury meets glamour. Each lash is designed to give your peepers that beautiful full lash look with added volume and glamour. Made from silk fibres and a flexible cotton band,you'll love the comfort!

Aurora -
Our lightest lash range yet! Made from ethically soured human hair,each lash oozes femininity and natural volume. You wont feel like your wearing lashes at all!

DewPoint Sponge-

Our innovative design makes blending creams or liquids a dream! Just dampen your sponge and apply your product to the skin. We recommend using the round side in bouncing motions to blend foundation and the flat side to push the product into the skin. The pointed end is specifically designed to get into those hard to reach areas,under eye area,around the nose etc.

Sponge cleaning instructions-( To be placed after lash imagery and descriptions.)

We recommend replacing your sponge every 6weeks. To clean your DewPoint Sponge,soak the sponge in hot soapy water and rinse until all makeup has been removed. Squeeze out excess water and allow to dry flat in a well ventilated room.

Information for end of brochure-
Visit www.dabandglow.example for prices and more information on all products.

Social media icons-
Facebook
Instagram
twitter

Choice of several brand logo jpeg and png.
Any further questions,we are happy to answer them.

Target Market(s)

Young,women

Industry/Entity Type

Hair And Beauty

Font styles to use
Other font styles liked:
• GeoSans Light

Colors
ecdaeb
eea4c8
e667a6
e34298
a64599
b868aa
000000
ffffff

Requirements
Must have
• Vibrant colour,sleek flow throughout brochure.
Should not have
• Images of people.

```html
<!DOCTYPE html>
<html lang="en">
<head>
<meta charset="utf-8">
<title>Dab&amp;Glow – Trifold Brochure</title>
<link rel="stylesheet" href="https://fonts.googleapis.com/css2?family=Montserrat:wght@400;500;600&family=Open+Sans:wght@400;600&family=Great+Vibes&display=swap">
<style>
  :root{
    --backdrop:#1a9cc4;
    --plum-deep:#160812;
    --plum:#3a0f33;
    --violet:#6a1a63;
    --orchid:#a64599;
    --mauve:#b868aa;
    --pink:#e34298;
    --rose:#e667a6;
    --blush:#eea4c8;
    --mist:#ecdaeb;
    --white:#ffffff;
    --ink:#000000;
    --body-grey:#3d3d3d;
  }
  *{box-sizing:border-box;margin:0;padding:0}
  html,body{width:850px;height:1200px;overflow:hidden}
  body{background:var(--backdrop);font-family:"Open Sans",sans-serif;position:relative}

  .sheet{position:absolute;left:35px;width:780px;height:560px;display:flex;box-shadow:0 10px 24px rgba(0,0,0,.3)}
  .sheet--outside{top:25px}
  .sheet--inside{top:615px}
  .panel{position:relative;width:260px;height:100%;overflow:hidden}
  .panel--dark{background:linear-gradient(180deg,var(--plum-deep) 0%,var(--plum) 45%,var(--violet) 100%);color:var(--white)}
  .panel--light{background:var(--white);color:var(--body-grey)}

  .brand-name{font-family:"Montserrat",sans-serif;font-weight:500;color:var(--pink);letter-spacing:.02em}

  /* Lashes panel */
  .corner-curve{position:absolute;top:0;left:0;width:260px;height:60px}
  .lashes{padding:58px 18px 0 22px}
  .lashes__title{font-family:"Montserrat",sans-serif;font-size:9px;letter-spacing:.3em;color:var(--pink);text-align:center;font-weight:600;margin-bottom:10px}
  .lashes__image{height:105px;border-radius:3px;background:linear-gradient(180deg,var(--white),var(--mist) 50%,var(--white));margin-bottom:14px}
  .sub-head{font-family:"Montserrat",sans-serif;font-size:8.5px;font-weight:600;color:var(--plum);margin:8px 0 4px}
  .copy{font-size:6.4px;line-height:1.45;text-align:justify}
  .copy strong{color:var(--plum)}
  .copy + .copy{margin-top:5px}

  /* Company panel */
  .company{padding:150px 22px 0 24px}
  .company__logo{text-align:center;font-size:28px;margin-bottom:50px}
  .company__label{font-family:"Montserrat",sans-serif;font-size:9px;color:var(--rose);margin-bottom:6px}
  .company__text{font-size:6.5px;line-height:1.5;text-align:justify;color:var(--mist);margin-bottom:22px}
  .company__lead{font-family:"Montserrat",sans-serif;font-size:10.5px;line-height:1.35;margin-bottom:22px}
  .company__lead em{font-style:normal;color:var(--pink)}
  .company__visit{font-family:"Montserrat",sans-serif;font-size:8px;line-height:1.6}
  .company__visit span{color:var(--pink)}
  .follow{position:absolute;left:24px;bottom:22px;font-family:"Montserrat",sans-serif;font-size:7px;display:flex;align-items:center;gap:4px}
  .dot{width:8px;height:8px;border-radius:50%;background:var(--white)}

  /* Cover panel */
  .cover__logo{position:absolute;top:40px;width:100%;text-align:center;font-size:26px}
  .cover__photo{position:absolute;top:120px;left:0;width:260px;height:300px;background:radial-gradient(ellipse at 50% 45%,#c9a27a 0%,#8a5a4c 40%,rgba(58,15,51,0) 75%)}
  .cover__curve{position:absolute;bottom:0;left:0;width:260px;height:150px}
  .cover__tagline{position:absolute;bottom:38px;width:100%;text-align:center}
  .script{font-family:"Great Vibes",cursive;font-size:22px;color:var(--pink);line-height:1}
  .cover__sub{font-family:"Montserrat",sans-serif;font-size:9.5px;font-weight:500;color:var(--plum);margin-top:2px}
  .cover__url{position:absolute;bottom:14px;width:100%;text-align:center;font-size:6px;letter-spacing:.25em;color:#777}

  /* Inside panels */
  .care{padding:22px 18px 0 20px}
  .care__head{font-family:"Montserrat",sans-serif;font-size:9px;color:var(--pink);margin:10px 0 4px}
  .care__head:first-child{margin-top:0}
  .care__text{font-size:6.4px;line-height:1.5;color:var(--mist);text-align:justify}
  .care__text--accent{color:var(--rose);margin:4px 0}
  .brush-photo{border-radius:3px;background:linear-gradient(90deg,var(--pink),var(--orchid),var(--pink),var(--mauve),var(--pink));opacity:.85}
  .care .brush-photo{height:80px;margin:14px 0 12px}
  .set{font-size:6.6px;line-height:1.5;color:var(--mist);margin-bottom:6px}
  .set b{color:var(--pink);font-family:"Montserrat",sans-serif;font-weight:500;font-size:7.5px}

  .individual{padding:20px 18px 0 20px}
  .individual__logo{text-align:center;font-size:24px;margin-bottom:10px}
  .individual__title{font-family:"Montserrat",sans-serif;font-size:9px;letter-spacing:.28em;color:var(--pink);text-align:center;margin-bottom:10px}
  .brush-item{font-size:6.5px;line-height:1.5;color:var(--mist);margin-bottom:7px}
  .brush-item b{color:var(--pink);font-weight:600}
  .individual__url{position:absolute;bottom:32px;width:100%;left:0;text-align:center;font-family:"Montserrat",sans-serif;font-size:7px;letter-spacing:.3em}
  .individual__dots{position:absolute;bottom:18px;width:100%;left:0;display:flex;justify-content:center;gap:4px}

  .more{padding:22px 18px 0 20px}
  .more .brush-photo{height:130px;margin:10px 0 14px;background:linear-gradient(90deg,var(--plum) 0,var(--orchid) 12%,var(--plum) 22%,var(--orchid) 34%,var(--plum) 46%,var(--orchid) 58%,var(--plum) 70%,var(--orchid) 82%,var(--plum) 100%)}
</style>
</head>
<body>

<!-- Outside spread -->
<section class="sheet sheet--outside">
  <article class="panel panel--light">
    <svg class="corner-curve" viewBox="0 0 260 60" preserveAspectRatio="none" aria-hidden="true">
      <path d="M0 0 H260 V8 C170 12 110 20 0 58 Z" fill="var(--violet)"/>
      <path d="M0 58 C110 20 170 12 260 8 V12 C170 16 110 26 0 60 Z" fill="var(--pink)"/>
    </svg>
    <div class="lashes">
      <h2 class="lashes__title">LASHES</h2>
      <div class="lashes__image" role="img" aria-label="Twelve false lash styles in three rows"></div>
      <h3 class="sub-head">3 LASH RANGES:</h3>
      <p class="copy"><strong>VelTrim :</strong> Luxury meets glamour. Each lash is designed to give your peepers that beautiful full lash look with added volume and glamour. Made from silk fibres and a flexible cotton band, you'll love the comfort!</p>
      <p class="copy"><strong>Aurora :</strong> Our lightest lash range yet! Made from ethically soured human hair, each lash oozes femininity and natural volume. You wont feel like your wearing lashes at all!</p>
      <h3 class="sub-head">DewPoint Sponge:</h3>
      <p class="copy">Our innovative design makes blending creams or liquids a dream! Just dampen your sponge and apply your product to the skin. We recommend using the round side in bouncing motions to blend foundation and the flat side to push the product into the skin. The pointed end is specifically designed to get into those hard to reach areas, under eye area, around the nose etc.</p>
      <h3 class="sub-head">Sponge cleaning instructions:</h3>
      <p class="copy">We recommend replacing your sponge every 6 weeks. To clean your DewPoint Sponge, soak the sponge in hot soapy water and rinse until all makeup has been removed. Squeeze out excess water and allow to dry flat in a well ventilated room.</p>
    </div>
  </article>

  <article class="panel panel--dark">
    <div class="company">
      <div class="company__logo brand-name">Dab&amp;Glow</div>
      <h3 class="company__label">Company description</h3>
      <p class="company__text">Established in 2015 by Professional Makeup Artist Maura Delaney, Dab&amp;Glow is one of Irelands leading cosmetic brands. We provide the beauty industry with incredibly high quality makeup brushes and Luxury Lashes.</p>
      <p class="company__lead"><em>Expertly design</em> by Maura and handmade using <em>incredibly high quality</em> natural and synthetic hair.</p>
      <p class="company__visit">Visit www.dabandglow.example<br><span>for prices and more information<br>on ALL PRODUCTS</span></p>
    </div>
    <div class="follow">FOLLOW US ON <i class="dot"></i><i class="dot"></i><i class="dot"></i></div>
  </article>

  <article class="panel panel--dark">
    <div class="cover__logo brand-name">Dab&amp;Glow</div>
    <div class="cover__photo" role="img" aria-label="Portrait photograph of a model with long wavy blonde hair"></div>
    <svg class="cover__curve" viewBox="0 0 260 150" preserveAspectRatio="none" aria-hidden="true">
      <path d="M0 40 C90 70 170 40 260 0 V150 H0 Z" fill="var(--pink)"/>
      <path d="M0 46 C90 76 170 46 260 6 V150 H0 Z" fill="var(--white)"/>
    </svg>
    <div class="cover__tagline">
      <div class="script">Professional, Vibrant</div>
      <div class="cover__sub">&amp; Modern Makeup Brushes</div>
    </div>
    <div class="cover__url">WWW.DABANDGLOW.EXAMPLE</div>
  </article>
</section>

<!-- Inside spread -->
<section class="sheet sheet--inside">
  <article class="panel panel--dark">
    <div class="care">
      <h3 class="care__head">Brush Care :</h3>
      <p class="care__text">Keep'em clean! To keep your brushes in their best shape possible, clean them once a week with warm soapy water. Avoid submerging the ferrule (metal part) in water as this could loosen the glue inside and cause the hair to shed. Shedding is normal for the first few washes. Rinse the brush well with clean water and air dry flat.</p>
      <h3 class="care__head">Lash Care :</h3>
      <p class="care__text">All our lashes are re-usable so take care of them and you will have fluttery long lashes for up to 30 wears!</p>
      <p class="care__text care__text--accent">We recommend cleaning your lashes after every 3 wears.</p>
      <p class="care__text">Firstly, remove any left over glue from the lash band and soak the lashes in warm soapy water for 5 minutes. Remove and rinse and residue from the lash. Re-shape and Replace the lash back into its case and let dry naturally. As good as new!</p>
      <div class="brush-photo" role="img" aria-label="Row of pink-handled makeup brushes"></div>
      <h3 class="care__head">BRUSH SETS :</h3>
      <p class="set"><b>Quite Rosy Glow :</b> Containing 8 professional brushes, this set is your go to for your everyday makeup application. DG01, DG02, DG03, DG04, DG05, DG06, DG10, DG24</p>
      <p class="set"><b>Top Lids Set :</b> Contain 8 of our incredible eye brushes for expert application. DG02, DG06, DG12, DG14, DG16, DG18, DG20, DG24</p>
      <p class="set"><b>Sharp Cheek set :</b> The ideal mix containing 6 of our most popular face and eye brushes. DG07, DG09, DG14, DG16, DG18, DG24.</p>
    </div>
  </article>

  <article class="panel panel--dark">
    <div class="individual">
      <div class="individual__logo brand-name">Dab&amp;Glow</div>
      <h2 class="individual__title">INDIVIDUAL BRUSHES</h2>
      <p class="brush-item"><b>DG01 :</b> Large synthetic powder brush. Ideal for use with powder foundations, creams or liquids.</p>
      <p class="brush-item"><b>DG02 :</b> Ideal for detailed eye work. Using ultra soft hair, it won't irritate the delicate eye area.</p>
      <p class="brush-item"><b>DG03 :</b> Domed shape, synthetic hair, the DG03 is perfect for seamlessly buffing liquid, creams, gel based foundations into the skin for a flawless finish.</p>
      <p class="brush-item"><b>DG04 :</b> Ultra soft synthetic hair, DG04 is a must have multi task brush. From concealer to eyeshadow application this all rounder is essential in the makeup bag.</p>
      <p class="brush-item"><b>DG05 :</b> Silky soft blush brush applies the perfect amount of product for flawless skin.</p>
      <p class="brush-item"><b>DG06 :</b> Precisely blends shadows into the socket of the eye for controlled blending.</p>
      <p class="brush-item"><b>DG08 :</b> <b>NEW!</b> Domed shadow blending brush, ideal for softening edges.</p>
      <p class="brush-item"><b>DG09 :</b> The unique tapered shape on our contour is perfect for chiseling out cheekbones or simply adding a pop of colour to the cheeks using the flat sides. (Synthetic)</p>
    </div>
    <div class="individual__url">WWW.DABANDGLOW.EXAMPLE</div>
    <div class="individual__dots"><i class="dot"></i><i class="dot"></i><i class="dot"></i></div>
  </article>

  <article class="panel panel--dark">
    <div class="more">
      <p class="brush-item"><b>DG10 :</b> Synthetic hair, DG10 is ultra thin with a precise angle, ideal for creating winged eyeliner or definition to brows.</p>
      <p class="brush-item"><b>DG12 :</b> Our finest blending brush yet! This truly is a must have for anyone who loves to add precise detail to their makeup looks. Super soft and light, it blends with ease for a flawless finish.</p>
      <p class="brush-item"><b>DG14 :</b> This is the ultimate brush for under eye blending! Dense, silky and sturdy, it is simply an essential in any eye look.</p>
      <p class="brush-item"><b>DG16 :</b> Another must have for any makeup bag is our flat shading brush. No more fall out from eyeshadows as this controls the placement perfectly. (Synthetic)</p>
      <div class="brush-photo" role="img" aria-label="Eight purple-handled eye brushes standing side by side"></div>
      <p class="brush-item"><b>DG18 :</b> If your looking to pack on colour to a specific area or to smudge out for a smokey effect this nifty little brush is one for the collection. (Synthetic)</p>
      <p class="brush-item"><b>DG20 :</b> An all rounder brush, our flat definer is a real multitasker. From defining the brows to cutting the crease there is no job too big or too small for the DG20. (Synthetic)</p>
      <p class="brush-item"><b>DG24 :</b> Ultra soft and dense. Hand crafted, tapered hair blends shadows effortlessly.</p>
    </div>
  </article>
</section>

</body>
</html>
```